依頼詳細
ノンシリコンスカルプシャンプー
頭皮をしっかり洗浄し傷ついた髪の毛を修復します。
またアロマ系の香りがリラックス効果を促します。
ユニセックスシャンプーですが女性向けでば珍しいブラックボトルを採用し、
Vornile(輝く私)の名称通りしなやかで芯のある女性をイメージしたパッケージラベル
記載項目
サイズ:W35㎜×P65㎜
防水シール
希望イメージ
シンプル 複雑
単色 カラフル
暗い 明るい
日常 高級
遊び心 厳粛
未来的 伝統的
女性的 男性的
希望する色
設定なし
納品ファイル
• 高解像度JPG (.jpg)
• イラストレーター形式 (.ai)
• フォトショップ形式 (.psd)
• PNG形式 (.png)
補足説明
設定なし
ボトルサイズ詳細について添付ファイルを追加しました
製品名『Vornile Premium Shampoo』の文字デザインをメインにお願いします。
参考までに他社のボトルラベルの画像をUPします。
文字だけのデザインを希望しています。
■ 選んだ理由

シャンプーを使った時に感じてもらうイメージがシンプルでスッキリとしたデザインとマッチしている点です。対象のお客様もほどんどが女性の為、女性らしい書体デザインが気に入りました。

■ 提案者全員のお礼・コメント

たくさんの方に提案を頂き本当に感謝しています。ありがとうございました。
選定には大変迷いましたが素敵なデザインをたくさん目にすることができて本当に良かったです。皆様の今後の活躍を心より祈願します。

```html
<!DOCTYPE html>
<html lang="en">
<head>
<meta charset="utf-8">
<title>Vornile Premium Labels</title>
<link rel="stylesheet" href="https://fonts.googleapis.com/css2?family=Amatic+SC:wght@400;700&family=Josefin+Sans:wght@300;400&display=swap">
<style>
  :root {
    --page: #f4f4f4;
    --grey-label: #b8b8b8;
    --white-label: #ffffff;
    --ink-dark: #2a2a2a;
    --ink-light: #ffffff;
    --rule-soft: #d6d6d6;
  }
  html, body {
    margin: 0;
    padding: 0;
    width: 846px;
    height: 1200px;
    overflow: hidden;
    background: var(--page);
  }
  .canvas {
    position: relative;
    width: 846px;
    height: 1200px;
    display: flex;
    justify-content: center;
    align-items: center;
    gap: 44px;
  }
  .label {
    width: 340px;
    height: 632px;
    box-sizing: border-box;
    display: flex;
    flex-direction: column;
    align-items: center;
    padding-top: 96px;
    box-shadow: 0 0 0 1px var(--rule-soft);
  }
  .label--shampoo {
    background: var(--grey-label);
    color: var(--ink-light);
    --rule: var(--ink-light);
  }
  .label--conditioner {
    background: var(--white-label);
    color: var(--ink-dark);
    --rule: var(--ink-dark);
  }
  .label__rule {
    width: 276px;
    height: 0;
    border-top: 2px solid var(--rule);
  }
  .label__title {
    margin: 22px 0 26px;
    font-family: "Amatic SC", sans-serif;
    font-weight: 400;
    font-size: 66px;
    line-height: 1.02;
    letter-spacing: 6px;
    text-align: center;
    text-transform: uppercase;
  }
  .label__tagline {
    margin-top: 20px;
    width: 276px;
    font-family: "Josefin Sans", sans-serif;
    font-weight: 300;
    font-size: 17px;
    line-height: 1.5;
    text-align: left;
    padding-left: 6px;
    box-sizing: border-box;
  }
  .label__volume {
    margin-top: auto;
    margin-bottom: 82px;
    font-family: "Josefin Sans", sans-serif;
    font-weight: 300;
    font-size: 17px;
    letter-spacing: 1px;
  }
</style>
</head>
<body>
  <main class="canvas">
    <section class="label label--shampoo">
      <div class="label__rule"></div>
      <h1 class="label__title">Vornile<br>Premium<br>Shampoo</h1>
      <div class="label__rule"></div>
      <p class="label__tagline">Non-Silicone<br>Scalp Care</p>
      <p class="label__volume">500ML</p>
    </section>
    <section class="label label--conditioner">
      <div class="label__rule"></div>
      <h1 class="label__title">Vornile<br>Premium<br>Conditioner</h1>
      <div class="label__rule"></div>
      <p class="label__tagline">Non-Silicone<br>Scalp Care</p>
      <p class="label__volume">500ML</p>
    </section>
  </main>
</body>
</html>
```